Everything fresh, everything new

When I take over the practice, I would like to breathe new life into the practice. I want a business card design that catches the eye and brings a breath of fresh air

```html
<!DOCTYPE html>
<html lang="en">
<head>
<meta charset="utf-8">
<title>Kinetika Business Card</title>
<link rel="stylesheet" href="https://fonts.googleapis.com/css2?family=Montserrat:wght@500;700&family=Arimo:wght@400&display=swap">
<style>
  :root {
    --stage: #1b1b1b;
    --card: #2b2b2b;
    --card-edge: #333333;
    --green: #8dc63f;
    --white: #f2f2f2;
    --muted: #d8d8d8;
  }
  * { margin: 0; padding: 0; box-sizing: border-box; }
  html, body { width: 1200px; height: 801px; overflow: hidden; background: var(--stage); }
  .stage {
    width: 1200px; height: 801px;
    display: flex; align-items: center; justify-content: center; gap: 48px;
  }
  .card {
    position: relative;
    width: 530px; height: 304px;
    border-radius: 22px;
    background: linear-gradient(135deg, var(--card-edge), var(--card));
    box-shadow: 0 18px 40px rgba(0,0,0,.55);
    overflow: hidden;
  }
  /* front */
  .brand {
    position: absolute; top: 36px; right: 40px;
    display: flex; align-items: center; gap: 10px;
    font-family: 'Montserrat', sans-serif; font-weight: 700;
    font-size: 30px; color: var(--white); letter-spacing: .3px;
  }
  .brand-dot { width: 14px; height: 14px; border-radius: 50%; background: var(--green); }
  .divider {
    position: absolute; left: 40px; right: 40px; top: 152px;
    height: 1px; background: var(--green);
  }
  .person {
    position: absolute; left: 40px; top: 100px;
    font-family: 'Montserrat', sans-serif;
  }
  .person-name { font-weight: 700; font-size: 24px; color: var(--green); letter-spacing: 1px; line-height: 1.05; }
  .person-role { font-family: 'Arimo', sans-serif; font-size: 15px; color: var(--white); margin-top: 2px; }
  .contacts {
    position: absolute; left: 40px; top: 168px;
    list-style: none;
    font-family: 'Arimo', sans-serif; font-size: 15px; color: var(--white);
  }
  .contacts li { display: flex; align-items: center; gap: 9px; line-height: 25px; }
  .contacts svg { width: 13px; height: 13px; flex: none; }
  .address {
    position: absolute; right: 40px; top: 172px; text-align: right; font-style: normal;
    font-family: 'Arimo', sans-serif; font-size: 15px; color: var(--white); line-height: 24px;
  }
  /* back */
  .back-name {
    position: absolute; inset: 0;
    display: flex; align-items: center; justify-content: center;
    font-family: 'Montserrat', sans-serif; font-weight: 700;
    font-size: 54px; color: var(--muted); letter-spacing: .5px;
  }
</style>
</head>
<body>
<main class="stage">
  <section class="card front">
    <div class="brand"><span class="brand-dot"></span>Kinetika</div>
    <div class="person">
      <p class="person-name">LENA HARTMANN</p>
      <p class="person-role">Owner/CEO</p>
    </div>
    <div class="divider"></div>
    <ul class="contacts">
      <li><svg viewBox="0 0 16 16"><path fill="#8dc63f" d="M3 1l3 3-2 2c1 2 3 4 5 5l2-2 3 3-2 3C7 15 1 9 1 3z"/></svg>210-555-0147</li>
      <li><svg viewBox="0 0 16 16"><rect x="4" y="1" width="8" height="14" rx="1.5" fill="none" stroke="#8dc63f" stroke-width="2"/></svg>210-555-0162</li>
      <li><svg viewBox="0 0 16 16"><rect x="1" y="3" width="14" height="10" fill="#8dc63f"/><path d="M1 3l7 6 7-6" fill="none" stroke="#2b2b2b" stroke-width="1.5"/></svg>info@kinetika-praxis.com</li>
      <li><svg viewBox="0 0 16 16"><circle cx="8" cy="8" r="6.5" fill="none" stroke="#8dc63f" stroke-width="2"/><path d="M1.5 8h13M8 1.5c-3 3-3 10 0 13M8 1.5c3 3 3 10 0 13" fill="none" stroke="#8dc63f" stroke-width="1.2"/></svg>www.kinetika-praxis.com</li>
    </ul>
    <address class="address">17 Lindenweg<br>Maple Falls, 40321</address>
  </section>
  <section class="card back">
    <p class="back-name">Kinetika</p>
  </section>
</main>
</body>
</html>
```